Business cards for Tile Contractor
Brisk Grout Studio
LAST MINUTE ADDITION TO BUSINESS CARD!!
website address: briskgroutstudio.net
and a space after the area code in phone number:
thanks!!
#85 is closest to what im looking for. Thanks for all the drafts! good stuff!
looks good so far. would like to see more with all the info on the card.

```html
<!DOCTYPE html>
<html lang="en">
<head>
<meta charset="utf-8">
<title>Brisk Grout Studio – Business Card</title>
<link rel="stylesheet" href="https://fonts.googleapis.com/css2?family=Open+Sans:wght@400;600;700&display=swap">
<style>
  :root {
    --page-bg: #ecebe8;
    --card-white: #ffffff;
    --navy-deep: #0a1f4d;
    --navy-mid: #12408a;
    --glow: #1ca4e0;
    --swoosh-grey: #b9bcc2;
    --brand-navy: #14306a;
    --text-light: #ffffff;
    --mark-faint: #e6eaf0;
  }
  html, body {
    margin: 0;
    padding: 0;
    width: 1200px;
    height: 935px;
    overflow: hidden;
    background: var(--page-bg);
    font-family: "Open Sans", Arial, sans-serif;
  }
  .business-card {
    position: absolute;
    left: 100px;
    top: 181px;
    width: 1000px;
    height: 572px;
    border-radius: 40px;
    overflow: hidden;
    background: var(--card-white);
    box-shadow: 0 10px 30px rgba(0,0,0,0.18);
  }
  .card-shapes {
    position: absolute;
    inset: 0;
  }
  .contact-name {
    position: absolute;
    left: 42px;
    top: 96px;
    margin: 0;
    color: var(--text-light);
    font-size: 30px;
    font-weight: 700;
    line-height: 40px;
  }
  .contact-title {
    position: absolute;
    left: 42px;
    top: 140px;
    margin: 0;
    color: var(--text-light);
    font-size: 19px;
    font-weight: 600;
    line-height: 26px;
  }
  .contact-details {
    position: absolute;
    left: 42px;
    top: 346px;
    margin: 0;
    color: var(--text-light);
    font-size: 21px;
    font-weight: 600;
    font-style: normal;
    line-height: 31px;
  }
  .brand {
    position: absolute;
    left: 492px;
    top: 80px;
    display: flex;
    align-items: center;
    gap: 16px;
  }
  .brand-dot {
    width: 54px;
    height: 54px;
    border-radius: 50%;
    background: var(--brand-navy);
  }
  .brand-name {
    margin: 0;
    color: var(--brand-navy);
    font-size: 41px;
    font-weight: 700;
    line-height: 1;
    white-space: nowrap;
  }
</style>
</head>
<body>
  <div class="business-card">
    <svg class="card-shapes" width="1000" height="572" viewBox="0 0 1000 572" aria-hidden="true">
      <defs>
        <radialGradient id="panelGlow" cx="150" cy="250" r="420" gradientUnits="userSpaceOnUse">
          <stop offset="0" stop-color="#1ca4e0"/>
          <stop offset="0.35" stop-color="#12408a"/>
          <stop offset="1" stop-color="#0a1f4d"/>
        </radialGradient>
      </defs>
      <path class="side-swoosh" d="M440,0 C320,150 350,390 575,572" fill="none" stroke="#b9bcc2" stroke-width="10"/>
      <path class="side-panel" d="M0,0 H420 C300,150 330,385 545,572 H0 Z" fill="url(#panelGlow)"/>
      <circle class="faint-mark" cx="760" cy="370" r="95" fill="#e6eaf0"/>
    </svg>

    <h1 class="contact-name">Rafe Dunmore</h1>
    <p class="contact-title">Owner/Tile Setter</p>
    <address class="contact-details">
      2217 E. Harlow Ave.<br>
      Monterey, Ca 93940<br>
      Phone: (831) 555-0147<br>
      Email : briskgroutstudio@ymail.com<br>
      Web : briskgroutstudio.net
    </address>

    <div class="brand">
      <span class="brand-dot"></span>
      <p class="brand-name">Brisk Grout Studio</p>
    </div>
  </div>
</body>
</html>
```